Website design for legal tech start up in Switzerland (B2B)

We are for a legal tech start up in Switzerland called TAVO. We have been running since August 2016. This will be our first live website.

We need a website designed and business card design for our start-up in Switzerland. We also need the Web design to be converted into HTML and CSS files.

Function of website:
• To inform potential customers of our services
• Form a key part of our digital marketing and sales footprint.
• Branding

Please find attached logo.
Updates

Project Deadline Extended Reason: Giving us time to review submissions and provide opportunity for more submissions. Added Thursday, February 16, 2017

Reason: Looking for more idea's not necessarily set on blue and grey colours only.

Target Market(s)

B2B tech powered legal services.

Industry/Entity Type

Legal

Contact Information for Business Card

Lean and slick design.

Coding

Coded - Design and coding required

Number of Pages Required

5+ page

Requirements
Must have
• VERY LEAN AND CLEAN DESIGN!
• We have received many great standard designs, but we are looking for something more out-of-the box: You can get inspiration from these designs: http://www.pindelsite.com/websites/clean/
• Thanks!!
• Easy content management system
• Well structured coding for additional development
• Responsive webpage for all types of devices
• SEO optimized
• Tabs (Home, services, team, careers, blog, contact us)
• Colour scheme complementary to logo
Nice to have
• Look and Design - Approachable, High-tech, Modern
• Easy to add chat bot capability in future
Should not have
• Too busy/ too much clutter
• Not take to long to load

```html
<!DOCTYPE html>
<html lang="en">
<head>
<meta charset="utf-8">
<title>TAVO – Legal Tech Start Up in Switzerland</title>
<link rel="stylesheet" href="https://fonts.googleapis.com/css2?family=Raleway:wght@300;400;500;600;700&display=swap">
<style>
  :root{
    --blue:#0f3f8c;
    --ink:#2b2b2b;
    --text:#555;
    --line:#bdbdbd;
    --soft:#f8f8f8;
    --white:#fff;
    --footer:#111;
  }
  *{box-sizing:border-box;margin:0;padding:0}
  html,body{width:1200px;height:2579px;overflow:hidden}
  body{font-family:"Raleway",sans-serif;color:var(--ink);background:var(--white);position:relative}
  section,header,footer{position:absolute;left:0;width:1200px}

  /* Navigation */
  .site-header{top:0;height:50px;background:var(--white);z-index:2}
  .brand{position:absolute;left:92px;top:7px;font-size:31px;font-weight:700;letter-spacing:1px;color:#222}
  .main-nav{position:absolute;left:538px;top:18px;display:flex}
  .main-nav a{font-size:12.5px;font-weight:500;color:#333;text-decoration:none;letter-spacing:.4px;margin-right:57px}
  .main-nav a.active{color:var(--blue)}
  .main-nav a:last-child{margin-right:0}

  /* Hero */
  .hero{top:50px;height:538px;
    background:
      radial-gradient(ellipse 300px 60px at 640px 500px,rgba(255,255,255,.9),transparent),
      radial-gradient(ellipse 260px 200px at 180px 120px,rgba(200,200,200,.55),transparent),
      radial-gradient(ellipse 300px 220px at 1050px 160px,rgba(205,205,205,.5),transparent),
      linear-gradient(180deg,#e4e4e4,#eeeeee 55%,#f3f3f3)}
  .hero-portrait{position:absolute;left:474px;top:58px;width:252px;height:252px;border-radius:50%;border:6px solid #f6f6f6;
    background:
      radial-gradient(circle at 58% 30%,#d9d9d9 0,#a9a9a9 22%,transparent 40%),
      radial-gradient(ellipse 90px 70px at 55% 78%,#f0f0f0,transparent),
      radial-gradient(circle at 18% 40%,#5e5e5e,transparent 35%),
      linear-gradient(160deg,#8a8a8a,#6f6f6f 45%,#9d9d9d 75%,#c4c4c4)}
  .hero-title{position:absolute;left:0;top:358px;width:1200px;text-align:center;font-size:38px;line-height:54px;font-weight:500;color:#3a3a3a;text-transform:uppercase}
  .hero-title strong{color:var(--blue);font-weight:600}

  /* Features */
  .features{top:588px;height:318px}
  .feature{position:absolute;top:66px;width:302px}
  .feature-icon{position:absolute;left:0;top:0;width:34px;height:34px}
  .feature-kicker{margin-left:51px;font-size:15px;color:var(--blue);line-height:19px}
  .feature-title{margin-left:51px;font-size:18px;font-weight:500;color:#222;line-height:23px}
  .feature p{margin-top:20px;font-size:12.6px;line-height:19px;color:var(--text)}

  /* About */
  .about{top:906px;height:533px}
  .about-photo{position:absolute;left:0;top:0;width:600px;height:533px;
    background:
      radial-gradient(ellipse 120px 150px at 90px 370px,rgba(245,245,245,.95),transparent),
      radial-gradient(ellipse 150px 200px at 360px 230px,#3e5a86,transparent 75%),
      radial-gradient(ellipse 140px 80px at 330px 440px,#2e2e2e,transparent),
      radial-gradient(ellipse 180px 160px at 90px 130px,#5a3a22,transparent),
      linear-gradient(135deg,#3c3a2c,#5b5647 40%,#7c7a74 70%,#a8a7a3)}
  .about-frame{position:absolute;left:26px;top:29px;width:546px;height:474px;border:5px solid rgba(255,255,255,.6)}
  .about-panel{position:absolute;left:600px;top:0;width:600px;height:533px;background:var(--blue);color:var(--white);text-align:center;padding:180px 74px 0}
  .about-panel .eyebrow{font-size:15px;opacity:.9}
  .about-panel h2{font-size:31px;font-weight:500;margin-top:12px}
  .about-panel p{font-size:12.6px;line-height:19px;margin-top:30px}

  /* Team */
  .team{top:1439px;height:368px;background:var(--soft)}
  .team-intro{position:absolute;left:92px;top:78px;width:318px}
  .team-intro h2{font-size:31px;line-height:37px;font-weight:600;color:#222;text-transform:uppercase}
  .team-intro h2 span{display:block;color:var(--blue)}
  .team-intro p{margin-top:18px;font-size:12.6px;line-height:19px;color:var(--text)}
  .member{position:absolute;top:75px;width:205px;height:222px;
    background:
      radial-gradient(ellipse 70px 85px at 50% 45%,#c9c9c9,transparent),
      radial-gradient(ellipse 80px 45px at 50% 20%,#3a3a3a,transparent),
      radial-gradient(ellipse 110px 50px at 50% 100%,#5f5f5f,transparent),
      linear-gradient(180deg,#a5a5a5,#8d8d8d 60%,#7a7a7a)}
  .member-card{position:absolute;left:21px;top:21px;width:162px;height:181px;background:rgba(15,63,140,.93);color:var(--white);text-align:center;padding-top:62px}
  .member-card h3{font-size:16px;font-weight:500;text-transform:uppercase}
  .member-card .role{font-size:12.5px;margin-top:9px}
  .member-social{display:flex;justify-content:center;gap:10px;margin-top:36px}
  .icon-dot{width:14px;height:14px;border-radius:50%;border:1.5px solid var(--white)}

  /* Clients */
  .clients{top:1807px;height:362px;text-align:center}
  .clients .eyebrow{position:absolute;top:66px;width:1200px;font-size:15px;color:#444}
  .clients h2{position:absolute;top:92px;width:1200px;font-size:31px;font-weight:600;color:var(--blue)}
  .client{position:absolute;top:205px;width:260px;margin-left:-130px;display:flex;flex-direction:column;align-items:center;gap:12px;font-size:18px;font-weight:600;color:#666}
  .client .mark{width:44px;height:44px;border-radius:50%;background:#8f8f8f}
  .client.blue{color:var(--blue)}
  .client.blue .mark{background:var(--blue)}

  /* Contact */
  .contact{top:2169px;height:306px;background:var(--soft)}
  .map{position:absolute;left:0;top:0;width:597px;height:306px;
    background:
      radial-gradient(ellipse 160px 120px at 250px 170px,#e9e9e9,transparent),
      radial-gradient(ellipse 200px 140px at 480px 80px,#c7c7c7,transparent),
      radial-gradient(ellipse 180px 120px at 80px 250px,#c9c9c9,transparent),
      linear-gradient(135deg,#d6d6d6,#cdcdcd 50%,#dadada)}
  .map-pin{position:absolute;left:237px;top:146px;width:22px;height:30px}
  .contact-form{position:absolute;left:630px;top:0;width:542px;text-align:center}
  .contact-form .eyebrow{margin-top:38px;font-size:15px;color:#444}
  .contact-form h2{margin-top:8px;font-size:31px;font-weight:600;color:var(--blue)}
  .field{position:absolute;height:27px;border-bottom:1px solid var(--line);font-size:11.5px;color:#999;text-align:left;padding:8px 6px 0}
  .submit{position:absolute;left:206px;top:230px;width:118px;height:34px;background:var(--blue);color:var(--white);font-size:12.5px;line-height:34px;text-align:center}

  /* Footer */
  .site-footer{top:2475px;height:104px;background:var(--footer);color:var(--white);text-align:center}
  .footer-social{display:flex;justify-content:center;gap:32px;margin-top:25px}
  .footer-social .icon-dot{width:16px;height:16px}
  .copyright{font-size:12px;margin-top:17px}
  .credit{font-size:11px;color:#aaa;margin-top:5px}
</style>
</head>
<body>

<header class="site-header">
  <div class="brand">TAVO</div>
  <nav class="main-nav">
    <a class="active" href="#">HOME</a>
    <a href="#">SERVICES</a>
    <a href="#">TEAM</a>
    <a href="#">CAREERS</a>
    <a href="#">BLOG</a>
    <a href="#">CONTACT US</a>
  </nav>
</header>

<section class="hero" role="img" aria-label="Soft blurred office with a keyboard in the background">
  <div class="hero-portrait" role="img" aria-label="Round portrait of a smiling team member with colleagues at a desk"></div>
  <h1 class="hero-title">We are for a <strong>legal tech</strong><br><strong>start up</strong> in <strong>Switzerland</strong></h1>
</section>

<section class="features">
  <div class="feature" style="left:92px">
    <svg class="feature-icon" viewBox="0 0 34 34" fill="none" stroke="#0f3f8c" stroke-width="1.6"><circle cx="16" cy="14" r="11"/><ellipse cx="16" cy="14" rx="5" ry="11"/><path d="M5 14h22M7 8h18M7 20h18M16 25v6M10 31h12"/></svg>
    <div class="feature-kicker">Responsive</div>
    <div class="feature-title">Website Design</div>
    <p>Convexi et porrexerat obsistitur moles omni. Otia galeae subdita fuit di mixtam. Mundo vix formas sive toto ignea onerosior erectos. Sanctius adsiduis nisi uno. Regna verba gravitate foret coercuit terris. Lucis securae nitidis! Titan ventos umor tanto di cingebant partim cingebant conversa terra.</p>
  </div>
  <div class="feature" style="left:440px">
    <svg class="feature-icon" viewBox="0 0 34 34" fill="none" stroke="#0f3f8c" stroke-width="1.6"><path d="M5 29l14-14M9 3a7 7 0 0 0 8 10l14 14-3 3-14-14A7 7 0 0 1 4 8l4 4 4-1 1-4z"/><path d="M20 20l7 7"/></svg>
    <div class="feature-kicker">Legal Tech Start Up</div>
    <div class="feature-title">Website Development</div>
    <p>Convexi et porrexerat obsistitur moles omni. Otia galeae subdita fuit di mixtam. Mundo vix formas sive toto ignea onerosior erectos. Sanctius adsiduis nisi uno. Regna verba gravitate foret coercuit terris. Lucis securae nitidis! Titan ventos umor tanto di cingebant partim cingebant conversa terra.</p>
  </div>
  <div class="feature" style="left:787px">
    <svg class="feature-icon" viewBox="0 0 34 34" fill="none" stroke="#0f3f8c" stroke-width="1.6"><path d="M3 31h29M6 31V20M11 31V16M16 31V19M21 31V12M26 31V8M4 14l8-6 6 4 12-9"/></svg>
    <div class="feature-kicker">World's #1</div>
    <div class="feature-title">SEO Services</div>
    <p>Convexi et porrexerat obsistitur moles omni. Otia galeae subdita fuit di mixtam. Mundo vix formas sive toto ignea onerosior erectos. Sanctius adsiduis nisi uno. Regna verba gravitate foret coercuit terris. Lucis securae nitidis! Titan ventos umor tanto di cingebant partim cingebant conversa terra.</p>
  </div>
</section>

<section class="about">
  <div class="about-photo" role="img" aria-label="Man in a checked shirt working at a laptop beside printed charts"></div>
  <div class="about-frame"></div>
  <div class="about-panel">
    <div class="eyebrow">Et certis ille terrenae</div>
    <h2>About TAVO Company</h2>
    <p>Et certis ille terrenae obstabatque pinus iners? Mortales vix tanto fulminibus cornua metusque. Astra radiis? Mixta ab. Aere galeae deerat inposuit ne utramque habendum abscidit! Abscidit traxit oppida? Quod adspirate nova quinta. Quae aberant grandia finxit aetas norant. Passim consistere sublime zephyro in.</p>
  </div>
</section>

<section class="team">
  <div class="team-intro">
    <h2>Our <span>Team</span></h2>
    <p>Flamina grandia toto fixo nullus. Os nullo. Iunctarum tollere fixo alta aestu habentia prima litem rapidisque. Fert metusque orbe ensis iussit gentes spisso matutinis dixere</p>
  </div>
  <div class="member" style="left:440px" role="img" aria-label="Black and white portrait of a team member"></div>
  <div class="member" style="left:670px" role="img" aria-label="Black and white portrait of Ivo Marten">
    <div class="member-card">
      <h3>Ivo Marten</h3>
      <div class="role">Business Analyst</div>
      <div class="member-social"><span class="icon-dot"></span><span class="icon-dot"></span><span class="icon-dot"></span><span class="icon-dot"></span></div>
    </div>
  </div>
  <div class="member" style="left:902px" role="img" aria-label="Black and white portrait of a team member"></div>
</section>

<section class="clients">
  <div class="eyebrow">They worked with us</div>
  <h2>OUR CLIENTS</h2>
  <div class="client" style="left:210px"><span class="mark"></span>Corvel Law</div>
  <div class="client" style="left:469px"><span class="mark"></span>Harbord Law</div>
  <div class="client blue" style="left:727px"><span class="mark"></span>Lindqvist Law Group</div>
  <div class="client" style="left:985px"><span class="mark"></span>Meridian Counsel</div>
</section>

<section class="contact">
  <div class="map" role="img" aria-label="Grey street map of the city showing the office location">
    <svg class="map-pin" viewBox="0 0 22 30"><path d="M11 0a11 11 0 0 0-11 11c0 8 11 19 11 19s11-11 11-19A11 11 0 0 0 11 0z" fill="#1a1a1a"/><circle cx="11" cy="11" r="4" fill="#d6d6d6"/></svg>
  </div>
  <div class="contact-form">
    <div class="eyebrow">Please fill up the form</div>
    <h2>DROP US A MESSAGE</h2>
    <div class="field" style="left:0;top:125px;width:170px">full name</div>
    <div class="field" style="left:186px;top:125px;width:172px">email address</div>
    <div class="field" style="left:374px;top:125px;width:168px">phone number</div>
    <div class="field" style="left:0;top:170px;width:542px">message</div>
    <div class="submit">submit</div>
  </div>
</section>

<footer class="site-footer">
  <div class="footer-social"><span class="icon-dot"></span><span class="icon-dot"></span><span class="icon-dot"></span><span class="icon-dot"></span><span class="icon-dot"></span><span class="icon-dot"></span></div>
  <div class="copyright">Copyright 2017 TAVO | All rights reserved</div>
  <div class="credit">Designed &amp; developed by Northpine Studio</div>
</footer>

</body>
</html>
```